Keystone Approval Partners - Invitation for a get together

We are in need of an invitation for an upcoming gathering we are having with our clients. The gathering will be in Perrin's Bar in Manly. http://www.perrinsbar-example.com.au/. Perrins bar is described as a New York loft style bar.

We are a building and construction consulting firm, our clients include firms such as Tarvo Holt, Brisket Gate, Quorival.

We are seeking to thank our clients for their support with a Friday afternoon drinks at Perrins Bar. We will be providing food and drinks.

Details are:-

When - Friday 19 September 2014
Time - 4pm onwards
Where - 22 Fenwick Row Manly

I would like a map to appear on the invite indicating where the bar is. I would also like

Target Market(s)

Clients, such as property developers, architects, builders

Industry/Entity Type

Construction

Colors

Designer to choose colors to be used in the design.

Requirements
Must have
• Details of what the invite is for, i.e. Keystone Approval Partners invites you to Perrins Bar at Manly for a casual drink and get together.

Details of the event i.e. Date, time, Location
Nice to have
• We hope the invite will have a sophisticated feel about it, like a trendy New York bar

```html
<!DOCTYPE html>
<html lang="en">
<head>
<meta charset="utf-8">
<title>Keystone Approval Partners – Casual drink and get together</title>
<link rel="stylesheet" href="https://fonts.googleapis.com/css2?family=Lobster&family=Oswald:wght@500&family=Libre+Baskerville&display=swap">
<style>
  :root {
    --paper: #ffffff;
    --ink: #1f1c1c;
    --slate: #5d6b7a;
    --rule: #2a2727;
    --brand: #2f3b86;
    --script: "Lobster", cursive;
    --serif: "Libre Baskerville", Georgia, serif;
    --condensed: "Oswald", "Arial Narrow", sans-serif;
  }
  * { margin: 0; padding: 0; box-sizing: border-box; }
  html, body { width: 1200px; height: 783px; overflow: hidden; background: var(--paper); }
  .invite { position: relative; width: 1200px; height: 783px; color: var(--ink); }

  .arc-heading { position: absolute; left: 0; top: 0; width: 1200px; height: 140px; }
  .arc-heading text {
    font-family: var(--serif); font-size: 16px; letter-spacing: 3.5px;
    fill: var(--slate); text-transform: uppercase;
  }

  .venue-line {
    position: absolute; top: 104px; left: 0; width: 100%;
    text-align: center; font-size: 34px; line-height: 1;
  }
  .venue-line .place { font-family: var(--script); }
  .venue-line .small {
    font-family: var(--serif); font-size: 15px; letter-spacing: 2.5px;
    text-transform: uppercase; margin: 0 10px; vertical-align: 3px;
  }

  .headline {
    position: absolute; left: 0; width: 100%; text-align: center;
    font-family: var(--script); font-size: 104px; line-height: 1;
  }
  .headline--first { top: 186px; }
  .headline--second { top: 334px; }

  .conjunction {
    position: absolute; top: 305px; left: 50%; transform: translateX(-50%);
    font-family: var(--serif); font-size: 14px; letter-spacing: 2.5px;
    color: var(--slate); border-top: 1.5px solid var(--slate);
    border-bottom: 1.5px solid var(--slate); padding: 3px 3px 2px; line-height: 1;
  }

  .date-table {
    position: absolute; top: 483px; left: 12px; width: 1176px; height: 146px;
    display: flex; border-top: 1.5px solid var(--rule); border-bottom: 1.5px solid var(--rule);
  }
  .date-cell {
    display: flex; align-items: center; justify-content: center;
    border-left: 1.5px solid var(--rule); font-size: 106px; line-height: 1;
  }
  .date-cell:first-child { border-left: none; }
  .date-cell--day { width: 226px; font-family: var(--script); }
  .date-cell--num { width: 175px; font-family: var(--condensed); }
  .date-cell--month { width: 210px; font-family: var(--condensed); }
  .date-cell--year { width: 258px; font-family: var(--condensed); }
  .date-cell--time { flex: 1; font-family: var(--script); }

  .details {
    position: absolute; top: 664px; left: 0; width: 100%; text-align: center;
    font-family: var(--serif); font-size: 16px; letter-spacing: 2.5px; color: var(--slate);
  }

  .brand {
    position: absolute; top: 728px; left: 0; width: 100%;
    display: flex; align-items: center; justify-content: center; gap: 12px;
    font-family: var(--serif); font-size: 20px; color: var(--brand); letter-spacing: 1px;
  }
  .brand-mark { width: 30px; height: 30px; background: var(--brand); }
</style>
</head>
<body>
<main class="invite">
  <svg class="arc-heading" viewBox="0 0 1200 140" aria-label="Keystone Approval Partners invites you to">
    <path id="arc-path" d="M 250 128 Q 600 -22 950 128" fill="none"/>
    <text><textPath href="#arc-path" startOffset="50%" text-anchor="middle">Keystone Approval Partners invites you to</textPath></text>
  </svg>

  <p class="venue-line">
    <span class="place">Perrins Bar</span><span class="small">at</span><span class="place">Manly</span><span class="small">for a</span>
  </p>

  <h1 class="headline headline--first">Casual drink</h1>
  <span class="conjunction">AND</span>
  <h2 class="headline headline--second">Get together.</h2>

  <div class="date-table">
    <div class="date-cell date-cell--day">Fri</div>
    <div class="date-cell date-cell--num">19</div>
    <div class="date-cell date-cell--month">SEP</div>
    <div class="date-cell date-cell--year">2014</div>
    <div class="date-cell date-cell--time">4pm</div>
  </div>

  <p class="details">4pm onwards | 22 Fenwick Row Manly</p>

  <div class="brand">
    <span class="brand-mark"></span>
    <span class="brand-name">Keystone Approval Partners</span>
  </div>
</main>
</body>
</html>
```